Letterhead for Business Law Firm

We need a letter head for our firm based on the design we have settled on and it is attached. Our clients are small and large businesses around the world, and our letterhead is used typically for formal legal purposes such as demand letters (accusing the recipient of doing bad things) or responding to demand letters. It may also be sent to regulators and other government agencies. So this needs to be tasteful, but a little edgy as well - we try to convey that we are a firm that is different - businesses and investors come to us for creative, quick advice, typically in high stress circumstances, and for our ability to work through high conflict situations, and rapid paced engagements.

Target Market(s)

Lawyers, business executives, investors, government regulators who may receive letters from this firm on behalf of its clients.

Industry/Entity Type

Business

Requirements
Must have
• The design and the firm's contact information:
• Quillfen Law Firm, P.C.
• 8716 SW 19th Ave
• Portland, OR 97058
• phone: 971 555 0143
• fax: 971 555 0178
• in what placement and how depicted (e.g. a phone icon instead of the word "phone") I leave to your creative ideas.
Nice to have
• design and information can be placed at the top, bottom and/or sides of the letter, and the design should be for a standard letter size paper - and can have a separate design for the second page.

```html
<!DOCTYPE html>
<html lang="en">
<head>
<meta charset="utf-8">
<title>Quillfen Law Firm, P.C. — Letterhead</title>
<link rel="stylesheet" href="https://fonts.googleapis.com/css2?family=Arimo:wght@400&display=swap">
<style>
  :root {
    --paper: #ffffff;
    --ink: #1c1718;
    --storm-teal: #3e7d8a;
    --storm-dark: #1b1516;
    --rule-grey: #55595c;
    --footer-text: #ffffff;
  }
  * { margin: 0; padding: 0; box-sizing: border-box; }
  html, body { width: 848px; height: 1200px; overflow: hidden; background: var(--paper); }
  .letterhead {
    position: relative;
    width: 848px;
    height: 1200px;
    background: var(--paper);
    font-family: "Arimo", Arial, sans-serif;
    color: var(--ink);
  }
  .masthead {
    position: absolute;
    top: 57px; left: 0; width: 848px; height: 84px;
    display: flex; align-items: center; justify-content: center; gap: 16px;
  }
  .masthead__mark {
    width: 20px; height: 20px;
    background: var(--storm-teal);
    flex: none;
  }
  .masthead__name {
    font-size: 30px;
    font-weight: 400;
    letter-spacing: 7px;
    color: var(--ink);
    line-height: 1;
    white-space: nowrap;
  }
  .masthead__rule {
    position: absolute;
    top: 144px; left: 51px; width: 752px; height: 2px;
    background: linear-gradient(90deg, var(--storm-teal) 0%, var(--rule-grey) 45%, var(--storm-dark) 100%);
  }
  .contact-band {
    position: absolute;
    top: 1083px; left: 51px; width: 752px; height: 50px;
    background: linear-gradient(90deg, var(--storm-teal) 0%, #2a4a52 35%, var(--storm-dark) 65%, var(--storm-dark) 100%);
    color: var(--footer-text);
    font-size: 12px;
    line-height: 14px;
  }
  .contact-item {
    position: absolute;
    top: 5px;
    display: flex; flex-direction: column; align-items: center;
    white-space: nowrap;
  }
  .contact-item svg { width: 20px; height: 18px; margin-bottom: 6px; }
  .contact-item--address { left: 4px; }
  .contact-item--web { left: 338px; transform: translateX(-50%); }
  .contact-item--phone { left: 456px; transform: translateX(-50%); }
  .contact-item--fax { left: 556px; transform: translateX(-50%); }
  .contact-item--email { right: 4px; }
  .divider { display: inline-block; width: 1.5px; height: 14px; background: var(--footer-text); margin: 0 6px; vertical-align: -2px; }
  .storm-strip {
    position: absolute;
    top: 1141px; left: 51px; width: 752px; height: 22px;
    background: linear-gradient(90deg, #2b2728 0%, #4f7d87 25%, #2b2728 50%, #4f7d87 75%, #2b2728 100%);
  }
</style>
</head>
<body>
<div class="letterhead">
  <header class="masthead">
    <span class="masthead__mark"></span>
    <span class="masthead__name">QUILLFEN LAW FIRM, P.C.</span>
  </header>
  <div class="masthead__rule"></div>

  <footer class="contact-band">
    <div class="contact-item contact-item--address">
      <svg viewBox="0 0 20 18" fill="none" stroke="#fff" stroke-width="1.2">
        <rect x="1.5" y="3" width="17" height="12"/>
        <polyline points="1.5,3 10,10 18.5,3"/>
      </svg>
      <span>8716 SW 19th Ave<span class="divider"></span>Portland, OR 97058</span>
    </div>
    <div class="contact-item contact-item--web">
      <svg viewBox="0 0 20 18" fill="none" stroke="#fff" stroke-width="1.2">
        <circle cx="10" cy="9" r="7"/>
        <ellipse cx="10" cy="9" rx="3" ry="7"/>
        <line x1="3" y1="9" x2="17" y2="9"/>
        <line x1="4.5" y1="5" x2="15.5" y2="5"/>
        <line x1="4.5" y1="13" x2="15.5" y2="13"/>
      </svg>
      <span>www.quillfenlaw.com</span>
    </div>
    <div class="contact-item contact-item--phone">
      <svg viewBox="0 0 20 18" fill="#fff">
        <rect x="4" y="2" width="5" height="14" rx="1"/>
        <rect x="10" y="5" width="6" height="11" rx="1"/>
        <rect x="11.5" y="7" width="3" height="2" fill="#1b1516"/>
      </svg>
      <span>971 555 0143</span>
    </div>
    <div class="contact-item contact-item--fax">
      <svg viewBox="0 0 20 18" fill="none" stroke="#fff" stroke-width="1.2">
        <rect x="6" y="1.5" width="8" height="5"/>
        <rect x="2" y="6.5" width="16" height="7" rx="1"/>
        <rect x="6" y="11" width="8" height="5.5" fill="#1b1516"/>
      </svg>
      <span>971 555 0178</span>
    </div>
    <div class="contact-item contact-item--email">
      <svg viewBox="0 0 20 18">
        <text x="10" y="14" text-anchor="middle" font-family="Arimo, Arial, sans-serif" font-size="15" font-style="italic" fill="#fff">@</text>
      </svg>
      <span>office@quillfenlaw.com</span>
    </div>
  </footer>

  <div class="storm-strip" role="img" aria-label="Decorative strip of stormy sky tiles"></div>
</div>
</body>
</html>
```